Business cards, envelopes, etc. for real estate company

We have a finished logo for our real estate company. We need a corporate identity package with the following items:

1. Business Cards
2. Letterhead/Stationary - with 2 pages:
-1st page with full header
-2nd page without top header
3. Concise and professional e-mail signature image
4. Fax coversheet
5. Shipping label, with our return address and a mail-to address (on one label)

We need these to be editable. We don't know the industry standard for these items but perhaps you can provide them to us in .PDF and Word format (and if you use Adobe Illustrator for them, .AI as well).

Please use the attached placeholder logo in your design entry. We will provide you with the original logo to swap in (same size and design, just different text) when we choose your entry.

Please include the following information on the letterhead and business cards:

58 Birchwell Road
Suite 2B West
New York, NY 10587

Tel: 555-014-2837
Fax :555-014-2837

Please contact us if you have any questions about this contest.

Hi,

Thanks for your interest in this project. The logo to use should be working now. Please contact me if you have any further issues or questions.

I look forward to seeing your submissions. 

Hi,

We first wish to thank you all for your submissions. 

Here is some general feedback regarding the designs shown:

1. We would prefer square (as opposed to rounded) business cards.

2. For the fax coversheets, we are looking with a designed look. While we understand these are samples, we don't want it to appear as if it a standard block of text or a fax template from a word processing program.

3. For the 1st page of letterhead and envelopes, we do need an office address on them. The envelopes should have space for a stamp in the top right corner. We would prefer the envelopes not to have colored stripes.

4. We think a watermark of the logo is an interesting idea on the business cards and/or letterhead. This may be something to try. However, it is not strictly necessary and we would like to evaluate designs with and without it.

In general we are looking for a clean yet professional look.

We are actively reviewing all entries and thank you for your time and creativity.

One last comment: We understand making all objects in the brief takes some time. However, we want to remind all the designers that this contest is for more than just business cards (envelopes, letterheads, etc.) so if we choose your design, those items will be expected. Please refer to the original brief to see what we are requesting.

If you provide a mockup of any item listed in the brief (in addition to business cards) it would help us visualize your entire vision for this project.

```html
<!DOCTYPE html>
<html lang="en">
<head>
<meta charset="utf-8">
<title>Harlow &amp; Reed — Identity Set</title>
<link href="https://fonts.googleapis.com/css2?family=Arimo:wght@400;700&family=Open+Sans:wght@300;400&display=swap" rel="stylesheet">
<style>
:root{
  --navy:#1f3d5a;
  --brand-grey:#6d7073;
  --ink:#333;
  --label:#b3b3b3;
  --paper:#fff;
  --window:#f1ecec;
  --bg-top:#ececec;
  --bg-bottom:#bdbdbd;
}
*{box-sizing:border-box;margin:0;padding:0}
html,body{width:1200px;height:810px;overflow:hidden}
body{
  position:relative;
  background:radial-gradient(ellipse at 50% 0%,var(--bg-top) 0%,#d6d6d6 45%,var(--bg-bottom) 100%);
  font-family:"Arimo",Arial,sans-serif;color:var(--ink);
}
.item-label{position:absolute;font-size:19px;color:var(--label);transform:translateX(-50%);white-space:nowrap}
.sheet{position:absolute;background:var(--paper);box-shadow:0 3px 6px rgba(0,0,0,.35)}
.brand{position:absolute;display:flex;align-items:center;gap:4px}
.brand-square{background:var(--navy);flex:none}
.brand-name{font-family:"Open Sans",Arial,sans-serif;font-weight:400;color:var(--brand-grey);line-height:1.05}
.contact{position:absolute;text-align:right;font-size:5.2px;line-height:6.3px;color:var(--ink)}
.contact span{display:flex;justify-content:flex-end;align-items:center;gap:3px}
.contact i{display:inline-block;width:5px;height:5px;background:var(--navy)}
.band{position:absolute;left:0;right:0;background:var(--navy)}
.band-mark{position:absolute;background:var(--paper)}
.band-mark b{position:absolute;inset:3px 3px 0 3px;background:var(--navy)}

/* envelope */
.envelope{left:420px;top:63px;width:302px;height:192px;background:none;box-shadow:none}
.envelope .flap{position:absolute;left:0;top:0}
.envelope .body{position:absolute;left:0;top:50px;width:302px;height:142px;background:var(--paper);box-shadow:0 3px 6px rgba(0,0,0,.35)}
.envelope .window{position:absolute;left:160px;top:69px;width:107px;height:35px;border-radius:6px;background:var(--window)}

/* fax */
.fax-form{position:absolute;left:29px;top:88px;font-size:5.6px;line-height:11px;color:var(--ink)}
.fax-form u{display:inline-block;border-bottom:.6px solid #555;height:6px;vertical-align:baseline}
.fax-rule{position:absolute;left:29px;width:158px;border-top:.7px solid #777}
.fax-lines{position:absolute;left:29px;top:190px;width:243px}
.fax-lines div{border-top:.8px solid #8a8a8a;height:6.7px}
.fax-sign{position:absolute;left:29px;top:254px;font-size:5.6px;line-height:6px}
.fax-footer{position:absolute;left:0;right:0;top:325px;text-align:center;font-size:5.3px;line-height:7px}
.fax-footer strong{font-size:6.6px;display:block;line-height:9px}

/* cards */
.card-holder{position:absolute;left:10px;top:47px;font-size:5.4px;line-height:6px}
.card-holder strong{font-size:6.2px;display:block}
.card-holder small{font-size:3.4px;display:block;margin-bottom:4px}
.card-address{position:absolute;left:10px;top:66px;font-size:3.8px;line-height:4.7px}
.card-rule{position:absolute;left:10px;right:10px;top:54px;border-top:.6px solid #999}
</style>
</head>
<body>

<div class="item-label" style="left:576px;top:27px">Envelope</div>
<div class="sheet envelope">
  <svg class="flap" width="302" height="52" viewBox="0 0 302 52" aria-hidden="true">
    <path d="M6 0 H296 Q300 0 301 6 L302 52 H0 L1 6 Q2 0 6 0Z" fill="#1f3d5a"/>
  </svg>
  <div class="body">
    <div class="brand" style="left:15px;top:15px">
      <div class="brand-square" style="width:26px;height:26px"></div>
      <div class="brand-name" style="font-size:10.5px">Harlow<br>&amp; Reed</div>
    </div>
    <div class="contact" style="right:15px;top:14px">
      <span>555-014-2837<i></i></span><span>555-014-2837<i></i></span>
      <span>info@harlowreed.com<i></i></span><span>www.harlowreed.com<i></i></span>
    </div>
    <div class="window"></div>
    <div class="band" style="bottom:0;height:9px"></div>
    <div class="band-mark" style="left:251px;bottom:0;width:26px;height:17px"><b></b></div>
  </div>
</div>

<div class="sheet letterhead" style="left:74px;top:188px;width:291px;height:393px">
  <div class="brand" style="left:22px;top:20px">
    <div class="brand-square" style="width:28px;height:28px"></div>
    <div class="brand-name" style="font-size:11px">Harlow<br>&amp; Reed</div>
  </div>
  <div class="contact" style="right:18px;top:16px">
    <span>555-014-2837<i></i></span><span>555-014-2837<i></i></span>
    <span>info@harlowreed.com<i></i></span><span>www.harlowreed.com<i></i></span>
  </div>
  <div class="band" style="bottom:0;height:11px"></div>
  <div class="band-mark" style="left:248px;bottom:0;width:26px;height:20px"><b></b></div>
</div>
<div class="item-label" style="left:205px;top:594px">Letterhead</div>

<div class="sheet card-front" style="left:495px;top:294px;width:152px;height:87px">
  <div class="brand-square" style="position:absolute;left:56px;top:25px;width:39px;height:36px" role="img" aria-label="Harlow &amp; Reed"></div>
</div>

<div class="sheet card-back" style="left:495px;top:409px;width:152px;height:88px">
  <div class="brand" style="left:9px;top:9px">
    <div class="brand-square" style="width:20px;height:18px"></div>
    <div class="brand-name" style="font-size:8px">Harlow<br>&amp; Reed</div>
  </div>
  <div class="card-holder"><strong>Daniel Marsh</strong><small>Founder</small></div>
  <div class="card-rule"></div>
  <div class="card-address">58 Birchwell Road<br>Suite 2B West<br>New York, NY 10587</div>
  <div class="contact" style="right:10px;top:56px;font-size:3.8px;line-height:4.7px">
    <span>555-014-2837<i style="width:3.5px;height:3.5px"></i></span><span>555-014-2837<i style="width:3.5px;height:3.5px"></i></span>
    <span>info@harlowreed.com<i style="width:3.5px;height:3.5px"></i></span><span>www.harlowreed.com<i style="width:3.5px;height:3.5px"></i></span>
  </div>
</div>
<div class="item-label" style="left:574px;top:526px">Business Card</div>

<div class="sheet fax" style="left:775px;top:190px;width:301px;height:390px">
  <div class="brand" style="left:29px;top:24px">
    <div class="brand-square" style="width:30px;height:29px"></div>
    <div class="brand-name" style="font-size:13px">Harlow<br>&amp; Reed</div>
  </div>
  <div class="fax-form">
    DATE: <u style="width:48px"></u><br>
    TO: <u style="width:58px"></u><br>
    FROM: <u style="width:66px"></u><br>
    FAX NUMBER: <u style="width:45px"></u><br>
    TOTAL NUMBER OF PAGES: <u style="width:44px"></u> (including this page)<br>
    RE: [enter brief description of the fax]
  </div>
  <div class="fax-rule" style="top:152px;width:158px"></div>
  <div class="fax-sign" style="top:157px">Hello,</div>
  <div class="fax-sign" style="top:169px">[Body of fax]</div>
  <div class="fax-lines"><div></div><div></div><div></div><div></div><div></div><div></div><div></div><div></div><div></div><div></div></div>
  <div class="fax-sign" style="top:255px">Regards<br>Mr.Marsh</div>
  <div class="fax-footer">
    <strong>Harlow &amp; Reed</strong>
    58 Birchwell Road<br>Suite 2B West<br>New York, NY 10587<br>
    T: +555-014-2837 | F: +555-014-2837<br>
    E: info@harlowreed.com | W: www.harlowreed.com
  </div>
</div>
<div class="item-label" style="left:937px;top:594px">Fax Cover Sheet</div>

<div class="brand" style="left:905px;top:690px;gap:14px">
  <div class="brand-square" style="width:81px;height:67px"></div>
  <div class="brand-name" style="font-size:31px;line-height:35px">Harlow<br>&amp; Reed</div>
</div>

</body>
</html>
```